Brightfern Systems Business Cards

We need a new business card design for an Electrical company that also focuses on Audio Visual and Communications. We would like to see designs using our new company logo attached. The cards are for two different people outlined below. Full contact details will be provided when design winner is awarded, use generic information for now. Business card is to be double sided and we are open to layout and design ideas.

Target Market(s)

Residential & Commercial

Industry/Entity Type

Electrical

Contact Information for Business Card

Name: Corwin Bell - Senior Electrician, Name: Milo Grant - Technology Specialist.

Font styles to use
Sans Serif

Colors
0555a3
ffffff
000000

Requirements
Must have
• mobile number, email address, website address, PO Box address,
• A main heading somewhere on the card stating ELECTRICAL SERVICES - AUDIO VISUAL SALES & INSTALLATION - COMMUNICATIONS

```html
<!DOCTYPE html>
<html lang="en">
<head>
<meta charset="utf-8">
<title>Brightfern Systems – Business Card</title>
<link rel="stylesheet" href="https://fonts.googleapis.com/css2?family=Barlow+Condensed:wght@500;600;700&display=swap">
<style>
  :root {
    --brand-blue: #0555a3;
    --paper: #ffffff;
    --ink: #000000;
    --backdrop: #d9dadc;
    --edge: #e4e4e4;
  }
  * { box-sizing: border-box; margin: 0; padding: 0; }
  html, body {
    width: 1200px; height: 1000px; overflow: hidden;
    background: var(--backdrop);
    font-family: "Barlow Condensed", "Arial Narrow", sans-serif;
  }
  .sheet {
    width: 1200px; height: 1000px;
    display: flex; align-items: center; justify-content: center; gap: 90px;
  }
  .card {
    width: 360px; height: 572px;
    position: relative; overflow: hidden;
    border: 1px solid var(--edge);
    box-shadow: 0 6px 18px rgba(0,0,0,0.12);
  }
  /* Front side */
  .card--front {
    background: var(--brand-blue);
    display: flex; align-items: center; justify-content: center;
  }
  .wordmark {
    display: flex; align-items: center; gap: 12px;
    color: var(--paper);
  }
  .wordmark__dot {
    width: 26px; height: 26px; border-radius: 50%;
    background: var(--paper); flex: none;
  }
  .wordmark__name {
    font-weight: 600; font-size: 34px; line-height: 1;
    letter-spacing: 0.04em; text-transform: uppercase; white-space: nowrap;
  }
  /* Back side */
  .card--back { background: var(--paper); color: var(--ink); }
  .back__band {
    position: absolute; left: 0; right: 0; top: 120px; height: 160px;
    background: var(--brand-blue);
    display: flex; align-items: center; justify-content: center;
  }
  .back__band .wordmark__name { font-size: 30px; }
  .back__band .wordmark__dot { width: 22px; height: 22px; }
  .person {
    position: absolute; left: 0; right: 0; top: 306px; text-align: center;
  }
  .person__name {
    font-weight: 700; font-size: 30px; letter-spacing: 0.03em; line-height: 1;
  }
  .person__role {
    font-weight: 600; font-size: 13px; letter-spacing: 0.06em; margin-top: 6px;
  }
  .contact {
    position: absolute; left: 0; right: 0; top: 386px;
    list-style: none; text-align: center;
    font-weight: 500; font-size: 14px; line-height: 1.4; letter-spacing: 0.04em;
  }
  .services {
    position: absolute; left: 12px; right: 12px; bottom: 56px;
    font-weight: 600; font-size: 9px; line-height: 1.3; letter-spacing: 0.03em;
    text-transform: uppercase; text-align: center;
  }
</style>
</head>
<body>
<main class="sheet">
  <section class="card card--front" aria-label="Card front">
    <div class="wordmark">
      <span class="wordmark__dot"></span>
      <span class="wordmark__name">Brightfern Systems</span>
    </div>
  </section>

  <section class="card card--back" aria-label="Card back">
    <div class="back__band">
      <div class="wordmark">
        <span class="wordmark__dot"></span>
        <span class="wordmark__name">Brightfern Systems</span>
      </div>
    </div>
    <div class="person">
      <h1 class="person__name">CORWIN BELL</h1>
      <p class="person__role">SENIOR ELECTRICIAN</p>
    </div>
    <ul class="contact">
      <li>07000 555 0142</li>
      <li>CORWIN.BELL@BRIGHTFERN.COM</li>
      <li>WWW.BRIGHTFERN.COM</li>
      <li>PO BOX ADDRESS</li>
    </ul>
    <p class="services">Electrical Services · Audio Visual Sales &amp; Installation · Communications</p>
  </section>
</main>
</body>
</html>
```